Larkfield Health Marketing Flyer

We are a new medical practice in the community and need a flyer to send to other medical offices to inform of our services. We just completed our logo with PixelGuild and would like to incorporate that plus our marketing content into the flyer. Our medical practice has 2 divisions: (1)Mental Health/Psychiatry and (2) Migraine and Neurospasticity Management. Please see website for content and provider photos at www.WellLarkvale.com

Target Market(s)

Other Healthcare Professionals in the Community

Industry/Entity Type

Medical

Requirements
Must have
• Photos of all 5 healthcare providers, phone number, address, logo

```html
<!DOCTYPE html>
<html lang="en">
<head>
<meta charset="utf-8">
<title>Larkfield Health Flyer</title>
<link href="https://fonts.googleapis.com/css2?family=Montserrat:wght@400;500;600;700&display=swap" rel="stylesheet">
<style>
:root{
  --teal:#2fbfb3;
  --green:#a6cf4f;
  --dark:#333333;
  --text:#3f3f3f;
  --stage:#333333;
  --paper:#ffffff;
  --tint:#f1f7f6;
  --box:#e9f1de;
  --blob:#d3ebea;
}
*{box-sizing:border-box;margin:0;padding:0}
html,body{width:1200px;height:1200px;overflow:hidden;background:var(--stage);font-family:'Montserrat',sans-serif}
.flyer{position:absolute;left:210px;top:53px;width:780px;height:1093px;background:var(--paper);overflow:hidden;box-shadow:0 6px 24px rgba(0,0,0,.45)}
.abs{position:absolute}
.brand{left:24px;top:28px;width:240px;text-align:center}
.brand-dot{width:74px;height:74px;border-radius:50%;background:var(--teal);margin:0 auto 10px}
.brand-name{font-weight:600;color:var(--teal);line-height:1.05}
.brand-name .top{display:block;font-size:29px;letter-spacing:1.5px}
.brand-name .bottom{display:block;font-size:22px;letter-spacing:2px}
.headline{left:27px;top:183px;font-weight:700;font-size:37px;line-height:44px;color:var(--teal)}
.headline span{color:var(--green)}
.divisions{left:0;top:324px;width:780px;height:314px;background:var(--tint)}
.hero{left:0;top:0;width:780px;height:370px}
.intro{left:26px;top:333px;font-weight:700;font-size:15px;color:var(--dark)}
.blob{width:84px;height:64px;background:var(--blob);border-radius:48% 52% 44% 56%/55% 45% 55% 45%}
.division-title{font-weight:600;font-size:18.5px;line-height:23px;color:var(--teal);text-align:center}
.division-copy{font-size:13.6px;line-height:20.4px;color:var(--text);text-align:justify;text-align-last:center}
.rule-v{left:348px;top:460px;width:1px;height:160px;background:#e2ecea}
.providers-title{left:0;top:645px;width:780px;text-align:center;font-weight:700;font-size:20px;color:var(--green)}
.line{height:1.5px;background:var(--green)}
.provider{top:684px;width:140px;text-align:center}
.provider svg{display:block;margin:0 auto}
.pill{display:inline-block;margin-top:8px;background:var(--green);color:#fff;font-weight:600;font-size:14px;line-height:20px;padding:0 8px;border-radius:9px;white-space:nowrap}
.dots{left:110px;top:861px;width:574px;border-top:1.5px dashed #555}
.trait{top:874px;width:240px;height:99px;background:var(--box);border-radius:8px;text-align:center}
.trait-icon{width:48px;height:48px;margin:7px auto 6px;display:block}
.trait-label{font-weight:700;font-size:19px;color:var(--dark)}
.connect-tab{left:296px;top:990px;width:190px;height:26px}
.connect-label{left:296px;top:990px;width:190px;text-align:center;color:#fff;font-weight:700;font-size:21px;line-height:28px}
.band-dark{left:0;top:1014px;width:780px;height:5px;background:var(--dark)}
.footer{left:0;top:1019px;width:780px;height:74px;background:var(--teal)}
.contact{font-size:13.5px;color:#fff;display:flex;align-items:center;gap:6px;white-space:nowrap}
.contact .ic{width:14px;height:14px;border:1.2px solid #fff;border-radius:50%;flex:none}
.social-bar{width:2px;height:16px;background:#fff;margin-right:12px}
</style>
</head>
<body>
<div class="flyer">
  <div class="abs divisions"></div>

  <svg class="abs hero" viewBox="0 0 780 370">
    <defs>
      <linearGradient id="heroTone" x1="0" y1="0" x2=".6" y2="1">
        <stop offset="0" stop-color="#b7c3bf"/>
        <stop offset=".3" stop-color="#a77d55"/>
        <stop offset=".65" stop-color="#7a3f3a"/>
        <stop offset="1" stop-color="#5c5a33"/>
      </linearGradient>
    </defs>
    <path d="M305 0 C345 25 350 110 362 175 C385 290 490 362 600 364 C680 364 740 338 780 318 L780 0 Z" fill="var(--green)"/>
    <g role="img" aria-label="Photo of a smiling family with pumpkins at an autumn farm">
      <circle cx="582" cy="146" r="197" fill="url(#heroTone)"/>
    </g>
  </svg>

  <div class="abs brand">
    <div class="brand-dot"></div>
    <div class="brand-name"><span class="top">LARKFIELD</span><span class="bottom">HEALTH</span></div>
  </div>

  <h1 class="abs headline">Helping <span>Bodies</span><br>Helping <span>Minds</span><br>Helping <span>You</span></h1>

  <p class="abs intro">Our medical practice has 2 divisions:</p>

  <div class="abs blob" style="left:124px;top:376px"></div>
  <svg class="abs" style="left:122px;top:368px" width="90" height="76" viewBox="0 0 90 76" role="img" aria-label="Stethoscope icon">
    <g fill="none" stroke="var(--dark)" stroke-width="1.8" stroke-linecap="round">
      <path d="M10 4 C4 20 10 34 20 36 C30 34 34 20 28 4"/>
      <path d="M20 36 C20 50 16 66 30 68 C44 68 40 40 56 38 C62 38 66 40 68 44"/>
    </g>
    <circle cx="10" cy="4" r="1.8" fill="var(--dark)"/>
    <circle cx="28" cy="4" r="1.8" fill="var(--dark)"/>
    <circle cx="72" cy="44" r="5" fill="none" stroke="var(--dark)" stroke-width="1.6"/>
    <circle cx="72" cy="44" r="2" fill="var(--dark)"/>
  </svg>

  <div class="abs blob" role="img" aria-label="Dandelion illustration" style="left:524px;top:374px;background:linear-gradient(160deg,#d8eeed,#c7e5e3)"></div>

  <h2 class="abs division-title" style="left:26px;top:450px;width:292px">Mental Health/Psychiatry</h2>
  <p class="abs division-copy" style="left:26px;top:480px;width:292px">Bringing comprehensive evaluation, medication management and psycho-therapy to the full spectrum of mental health disorders including minor, moder-ate and major depression, bipolar disor-der, ADD/ADHD, anxiety, schizophrenia, stress or grief reactions, and others</p>

  <div class="abs rule-v"></div>

  <h2 class="abs division-title" style="left:374px;top:450px;width:382px">Migraine and Neurospasticity<br>Management</h2>
  <p class="abs division-copy" style="left:374px;top:501px;width:382px">Injections of botulinum neurotoxin are a widely used therapeutic form of treatment for both chronic migraines and patients with involuntary muscle con-tractions (neurospasticity). Injections may offer up to 3 months of relief and may be combined with other pharmaceutical interventions for maximum benefit</p>

  <h2 class="abs providers-title">Meet Our Providers</h2>
  <div class="abs line" style="left:110px;top:659px;width:168px"></div>
  <div class="abs line" style="left:504px;top:659px;width:168px"></div>

  <svg width="0" height="0" style="position:absolute">
    <defs>
      <radialGradient id="studioA" cx=".5" cy=".4" r=".7"><stop offset="0" stop-color="#c3c8cc"/><stop offset="1" stop-color="#7f878d"/></radialGradient>
      <radialGradient id="studioB" cx=".5" cy=".4" r=".7"><stop offset="0" stop-color="#8a7568"/><stop offset="1" stop-color="#3e4346"/></radialGradient>
      <radialGradient id="studioC" cx=".5" cy=".4" r=".7"><stop offset="0" stop-color="#a89a90"/><stop offset="1" stop-color="#4f575c"/></radialGradient>
      <radialGradient id="studioD" cx=".5" cy=".4" r=".7"><stop offset="0" stop-color="#c9c5c2"/><stop offset="1" stop-color="#6f7a7e"/></radialGradient>
      <radialGradient id="studioE" cx=".5" cy=".4" r=".7"><stop offset="0" stop-color="#d9c3a8"/><stop offset="1" stop-color="#7a5233"/></radialGradient>
    </defs>
  </svg>

  <div class="abs provider" style="left:31px">
    <svg width="128" height="132" viewBox="0 0 128 132"><polygon points="58,4 112,34 112,96 58,126 4,96 4,34" fill="var(--teal)" stroke="var(--teal)" stroke-width="8" stroke-linejoin="round"/><polygon points="68,6 122,36 122,98 68,128 14,98 14,36" fill="none" stroke="var(--green)" stroke-width="1.5" stroke-linejoin="round"/><polygon role="img" aria-label="Portrait of Evan Marlow" points="64,10 114,38 114,94 64,122 14,94 14,38" fill="url(#studioA)" stroke="url(#studioA)" stroke-width="6" stroke-linejoin="round"/></svg>
    <span class="pill">Evan Marlow</span>
  </div>
  <div class="abs provider" style="left:177px">
    <svg width="128" height="132" viewBox="0 0 128 132"><polygon points="70,4 124,34 124,96 70,126 16,96 16,34" fill="var(--teal)" stroke="var(--teal)" stroke-width="8" stroke-linejoin="round"/><polygon points="60,2 114,32 114,94 60,124 6,94 6,32" fill="none" stroke="var(--green)" stroke-width="1.5" stroke-linejoin="round"/><polygon role="img" aria-label="Portrait of Sienna Holt" points="64,10 114,38 114,94 64,122 14,94 14,38" fill="url(#studioB)" stroke="url(#studioB)" stroke-width="6" stroke-linejoin="round"/></svg>
    <span class="pill">Sienna Holt</span>
  </div>
  <div class="abs provider" style="left:320px">
    <svg width="128" height="132" viewBox="0 0 128 132"><polygon points="58,4 112,34 112,96 58,126 4,96 4,34" fill="var(--teal)" stroke="var(--teal)" stroke-width="8" stroke-linejoin="round"/><polygon points="68,6 122,36 122,98 68,128 14,98 14,36" fill="none" stroke="var(--green)" stroke-width="1.5" stroke-linejoin="round"/><polygon role="img" aria-label="Portrait of Reid Calder" points="64,10 114,38 114,94 64,122 14,94 14,38" fill="url(#studioC)" stroke="url(#studioC)" stroke-width="6" stroke-linejoin="round"/></svg>
    <span class="pill">Reid Calder</span>
  </div>
  <div class="abs provider" style="left:464px">
    <svg width="128" height="132" viewBox="0 0 128 132"><polygon points="70,4 124,34 124,96 70,126 16,96 16,34" fill="var(--teal)" stroke="var(--teal)" stroke-width="8" stroke-linejoin="round"/><polygon points="60,2 114,32 114,94 60,124 6,94 6,32" fill="none" stroke="var(--green)" stroke-width="1.5" stroke-linejoin="round"/><polygon role="img" aria-label="Portrait of Marian Fenwick" points="64,10 114,38 114,94 64,122 14,94 14,38" fill="url(#studioD)" stroke="url(#studioD)" stroke-width="6" stroke-linejoin="round"/></svg>
    <span class="pill">Marian Fenwick</span>
  </div>
  <div class="abs provider" style="left:609px">
    <svg width="128" height="132" viewBox="0 0 128 132"><polygon points="58,4 112,34 112,96 58,126 4,96 4,34" fill="var(--teal)" stroke="var(--teal)" stroke-width="8" stroke-linejoin="round"/><polygon points="68,6 122,36 122,98 68,128 14,98 14,36" fill="none" stroke="var(--green)" stroke-width="1.5" stroke-linejoin="round"/><polygon role="img" aria-label="Portrait of Dr. Paul Ostrander" points="64,10 114,38 114,94 64,122 14,94 14,38" fill="url(#studioE)" stroke="url(#studioE)" stroke-width="6" stroke-linejoin="round"/></svg>
    <span class="pill">Dr. Paul Ostrander</span>
  </div>

  <div class="abs dots"></div>

  <div class="abs trait" style="left:23px">
    <svg class="trait-icon" viewBox="0 0 40 40"><path d="M13 24 L8 36 L13 33 L16 37 L19 28 Z M27 24 L32 36 L27 33 L24 37 L21 28 Z" fill="var(--dark)"/><circle cx="20" cy="16" r="14" fill="var(--teal)"/><circle cx="20" cy="16" r="9" fill="none" stroke="#fff" stroke-width="2"/><path d="M15.5 16 L19 19.5 L25 13" fill="none" stroke="#fff" stroke-width="2.4" stroke-linecap="round"/></svg>
    <div class="trait-label">Board Certified</div>
  </div>
  <div class="abs trait" style="left:270px">
    <svg class="trait-icon" viewBox="0 0 40 40"><path d="M18 6 A13 12 0 0 1 37 15" fill="none" stroke="var(--dark)" stroke-width="4"/><path d="M20 0 L12 6 L21 11 Z" fill="var(--dark)"/><ellipse cx="19" cy="23" rx="17" ry="12" fill="var(--green)"/><path d="M7 31 L4 39 L14 33 Z" fill="var(--green)"/><g fill="#fff"><circle cx="13" cy="23" r="1"/><circle cx="17" cy="23" r="1"/><circle cx="21" cy="23" r="1"/><circle cx="25" cy="23" r="1"/></g></svg>
    <div class="trait-label">Responsive</div>
  </div>
  <div class="abs trait" style="left:516px">
    <svg class="trait-icon" viewBox="0 0 40 40"><path d="M20 37 L4 21 A9 9 0 0 1 20 8 Z" fill="var(--dark)"/><path d="M20 37 L36 21 A9 9 0 0 0 20 8 Z" fill="var(--teal)"/><path d="M12 24 L20 16 L28 22" fill="none" stroke="#fff" stroke-width="2"/></svg>
    <div class="trait-label">Compassionate</div>
  </div>

  <svg class="abs connect-tab" viewBox="0 0 190 26"><path d="M0 26 C10 26 12 0 30 0 L160 0 C178 0 180 26 190 26 Z" fill="var(--dark)"/></svg>
  <div class="abs connect-label">Let’s Connect</div>
  <div class="abs band-dark"></div>
  <div class="abs footer"></div>

  <div class="abs contact" style="left:24px;top:1030px">
    <svg width="14" height="14" viewBox="0 0 14 14"><circle cx="7" cy="7" r="6.3" fill="none" stroke="#fff" stroke-width="1.2"/><path d="M4.5 4 L6 3.8 L6.5 5.6 L5.7 6.2 A5 5 0 0 0 7.8 8.3 L8.4 7.5 L10.2 8 L10 9.5 A6 6 0 0 1 4.5 4 Z" fill="#fff"/></svg>
    208-555-0147
  </div>
  <div class="abs contact" style="left:24px;top:1053px">
    <svg width="14" height="14" viewBox="0 0 14 14"><circle cx="7" cy="7" r="6.3" fill="none" stroke="#fff" stroke-width="1.2"/><circle cx="7" cy="7" r="3.6" fill="none" stroke="#fff" stroke-width="1"/><path d="M3.4 7 H10.6 M7 3.4 V10.6" stroke="#fff" stroke-width="1"/></svg>
    www.WellLarkvale.com
  </div>
  <div class="abs contact" style="left:290px;top:1030px">
    <svg width="14" height="14" viewBox="0 0 14 14"><circle cx="7" cy="7" r="6.3" fill="none" stroke="#fff" stroke-width="1.2"/><rect x="3.8" y="4.8" width="6.4" height="4.6" fill="none" stroke="#fff" stroke-width="1"/><path d="M3.8 4.8 L7 7.4 L10.2 4.8" fill="none" stroke="#fff" stroke-width="1"/></svg>
    support@LarkfieldHealth.com
  </div>
  <div class="abs contact" style="left:290px;top:1053px">
    <svg width="14" height="14" viewBox="0 0 14 14"><circle cx="7" cy="7" r="6.3" fill="none" stroke="#fff" stroke-width="1.2"/><path d="M7 11 L4.6 7 A2.6 2.6 0 1 1 9.4 7 Z" fill="none" stroke="#fff" stroke-width="1"/><circle cx="7" cy="5.9" r=".9" fill="#fff"/></svg>
    415 W. Maple Crest Dr, Suite B, Cedar Falls, ID&nbsp; 83890
  </div>
  <div class="abs contact" style="left:630px;top:1030px">
    <span class="social-bar"></span>Social Media:&nbsp;&nbsp;<span class="ic"></span>
  </div>
</div>
</body>
</html>
```